Design an investor pitch deck for Brindlework.io

We delivered a killer investor pitch to a group of investors last week and have been asked for a deck. we need to follow up with a killer printed version. I have produced the attached file using free images from fotovane. Feel free to change the imagery as you see fit. Check out brindlework.io to get a feel for the look and feel we have right now.

Target Market(s)

Investors

Industry/Entity Type

Software

Font styles to use
Sans Serif
Other font styles liked:
• Helvetica

Requirements
Must have
• A new version of each of the pages in the example documents. Needs to be slick and professional
Nice to have
• Other layouts in case I add further slides
Should not have
• Childish or dated shapes or designs

```html
<!DOCTYPE html>
<html lang="en">
<head>
<meta charset="utf-8">
<title>Brindlework — Investor Deck Title</title>
<link rel="stylesheet" href="https://fonts.googleapis.com/css2?family=Questrial&display=swap">
<style>
  :root {
    --ink-white: #ffffff;
    --soft-white: rgba(255, 255, 255, 0.94);
    --photo-deep: #1c2a55;
    --photo-mid: #3b5292;
    --photo-light: #8799c4;
    --photo-haze: #a9b6d6;
  }
  * { margin: 0; padding: 0; box-sizing: border-box; }
  html, body {
    width: 1200px;
    height: 675px;
    overflow: hidden;
    background: var(--photo-deep);
  }
  .slide {
    position: relative;
    width: 1200px;
    height: 675px;
    overflow: hidden;
    font-family: "Questrial", "Century Gothic", sans-serif;
    color: var(--ink-white);
  }
  .hero-photo {
    position: absolute;
    inset: 0;
    background:
      radial-gradient(ellipse 55% 60% at 92% 20%, var(--photo-haze) 0%, rgba(169,182,214,0) 70%),
      radial-gradient(ellipse 40% 70% at 45% 55%, rgba(40,58,120,0.85) 0%, rgba(40,58,120,0) 75%),
      linear-gradient(100deg, var(--photo-mid) 0%, #4a62a3 35%, #5b70aa 60%, var(--photo-light) 85%, #6d7fb0 100%);
  }
  .hero-photo::after {
    content: "";
    position: absolute;
    inset: 0;
    background: linear-gradient(180deg, rgba(28,42,85,0) 55%, rgba(28,42,85,0.6) 100%);
  }
  .deck-title {
    position: absolute;
    left: 40px;
    top: 8px;
    font-size: 148px;
    font-weight: 400;
    line-height: 1;
    letter-spacing: 1px;
    color: var(--ink-white);
  }
  .tagline {
    position: absolute;
    left: 43px;
    top: 320px;
    font-size: 38px;
    font-weight: 400;
    color: var(--soft-white);
  }
  .byline {
    position: absolute;
    left: 43px;
    top: 421px;
    font-size: 26px;
    color: var(--soft-white);
    white-space: nowrap;
  }
  .byline .divider { margin: 0 6px; }
  .footer-rule {
    position: absolute;
    left: 0;
    top: 620px;
    width: 1102px;
    height: 2px;
    background: var(--ink-white);
  }
  .brand-mark {
    position: absolute;
    left: 1103px;
    top: 574px;
    width: 56px;
    height: 56px;
  }
  .brand-name {
    position: absolute;
    right: 110px;
    top: 592px;
    font-size: 16px;
    color: var(--ink-white);
  }
</style>
</head>
<body>
  <main class="slide">
    <div class="hero-photo" role="img" aria-label="Blue-toned photo of a man in a denim shirt checking his wristwatch outdoors at dusk"></div>

    <h1 class="deck-title">Brindlework</h1>
    <p class="tagline">Waiting sucks. Brindlework makes it better</p>
    <p class="byline">Marcus Hale<span class="divider">|</span>Founder @ Tallow Systems<span class="divider">|</span>marcus@brindlework.io</p>

    <div class="footer-rule"></div>
    <span class="brand-name">Brindlework</span>
    <svg class="brand-mark" viewBox="0 0 56 56" aria-hidden="true">
      <circle cx="28" cy="28" r="26" fill="none" stroke="#ffffff" stroke-width="3"/>
    </svg>
  </main>
</body>
</html>
```